Mobile Ultrasound Business
Coastal Imaging Partners of Brazos, LLC
Project: Mobile Ultrasound Business
Mobile Ultrasound Business - Health
Creative Brief
Professional
no address (company is mobile)
361-482-9031 (WAVE)
cipbz4@mailvelo.com
www.cipbzllc.com

```html
<!DOCTYPE html>
<html lang="en">
<head>
<meta charset="utf-8">
<title>Coastal Imaging Partners of Brazos – Stationery</title>
<link href="https://fonts.googleapis.com/css2?family=Open+Sans:wght@400;600;700&display=swap" rel="stylesheet">
<style>
:root{
  --bg:#e6e9ec;
  --paper:#ffffff;
  --blue:#1f7fd1;
  --blue-dark:#1766ab;
  --green:#5fb548;
  --ink:#4a4f55;
  --ink-soft:#9aa1a8;
  --shadow:0 3px 8px rgba(0,0,0,.18);
}
*{margin:0;padding:0;box-sizing:border-box}
html,body{width:1200px;height:373px;overflow:hidden;background:var(--bg);font-family:"Open Sans",Arial,sans-serif;color:var(--ink)}
.canvas{position:relative;width:1200px;height:373px}
.piece{position:absolute;background:var(--paper);box-shadow:var(--shadow)}
.brand{display:flex;align-items:center;gap:4px;color:var(--blue);font-weight:700;line-height:1.1}
.brand .mark{flex:none;background:var(--green)}

/* letterhead */
.letterhead{left:22px;top:92px;width:158px;height:206px;padding:12px 12px;z-index:2;font-size:4.2px;line-height:1.45}
.letterhead .brand{font-size:6px;width:80px}
.letterhead .brand .mark{width:9px;height:9px}
.letterhead .body{margin-top:14px}
.letterhead .body p{margin-bottom:4px}
.letterhead .sign{margin-top:8px}
.letterhead .footer{position:absolute;left:12px;right:12px;bottom:8px;border-top:1px solid var(--blue);padding-top:3px;color:var(--ink-soft);display:flex;justify-content:space-between}

/* envelope */
.envelope{left:168px;top:160px;width:170px;height:110px;z-index:1;overflow:hidden}
.envelope .brand{position:absolute;left:36px;top:8px;font-size:4.5px;width:70px}
.envelope .brand .mark{width:7px;height:7px}
.envelope .band{position:absolute;left:0;right:0;bottom:0;height:42px;background:var(--blue)}

/* business cards */
.card{width:84px;height:48px;padding:5px;overflow:hidden}
.card .brand{font-size:4.2px;width:74px}
.card .brand .mark{width:7px;height:7px}
.card-front{left:350px;top:114px}
.card-front .contact{margin-top:4px;font-size:3.2px;line-height:1.35;color:var(--ink)}
.card-front .contact strong{color:var(--blue);font-size:3.6px}
.card-white{left:350px;top:178px;display:flex;align-items:center;justify-content:center}
.card-blue{left:350px;top:236px;background:var(--blue);display:flex;align-items:center;justify-content:center}
.card-white .brand,.card-blue .brand{width:60px}
.card-blue .brand{color:var(--paper)}
.card-blue .brand .mark{background:var(--paper)}

/* closed folder */
.folder-front{left:570px;top:74px;width:140px;height:282px;overflow:hidden}
.folder-front .brand{position:absolute;left:22px;top:66px;font-size:11px;width:100px}
.folder-front .brand .mark{width:16px;height:16px}
.folder-front .flap{position:absolute;left:0;right:0;bottom:0;height:50px;background:var(--blue)}

/* open folder */
.folder-open{left:724px;top:74px;width:320px;height:282px;background:transparent;box-shadow:none}
.folder-open .panel{position:absolute;top:0;width:160px;height:282px;background:var(--paper);box-shadow:var(--shadow)}
.folder-open .left{left:0}
.folder-open .right{left:160px}
.folder-open .pocket{position:absolute;left:0;right:0;bottom:0;height:92px;background:var(--blue)}
.folder-open .left .pocket{clip-path:polygon(0 30%,100% 0,100% 100%,0 100%)}
.folder-open .right .pocket{clip-path:polygon(0 0,100% 30%,100% 100%,0 100%)}
.folder-open .slot-card{position:absolute;left:70px;bottom:70px;width:72px;height:40px;background:var(--paper);box-shadow:var(--shadow);padding:5px;display:flex;align-items:center}
.folder-open .slot-card .brand{font-size:4.2px;width:58px}
.folder-open .slot-card .brand .mark{width:6px;height:6px}
</style>
</head>
<body>
<main class="canvas">

  <section class="piece letterhead">
    <div class="brand"><span class="mark"></span><span>Coastal Imaging Partners of Brazos, LLC</span></div>
    <div class="body">
      <p>Dear Patient,</p>
      <p>Thank you for choosing our mobile ultrasound service. Our registered sonographers bring clear, accurate imaging directly to your clinic or home, on your schedule.</p>
      <p>We look forward to caring for you and your family.</p>
      <p class="sign">Sincerely,<br><strong>Mara Verlo</strong><br>Lead Sonographer</p>
    </div>
    <div class="footer"><span>361-482-9031 (WAVE)</span><span>cipbz4@mailvelo.com</span><span>www.cipbzllc.com</span></div>
  </section>

  <section class="piece envelope">
    <div class="brand"><span class="mark"></span><span>Coastal Imaging Partners of Brazos, LLC</span></div>
    <div class="band"></div>
  </section>

  <section class="piece card card-front">
    <div class="brand"><span class="mark"></span><span>Coastal Imaging Partners of Brazos, LLC</span></div>
    <div class="contact">
      <strong>Mara Verlo</strong><br>Lead Sonographer<br>
      361-482-9031 (WAVE)<br>cipbz4@mailvelo.com<br>www.cipbzllc.com
    </div>
  </section>

  <section class="piece card card-white">
    <div class="brand"><span class="mark"></span><span>Coastal Imaging Partners of Brazos, LLC</span></div>
  </section>

  <section class="piece card card-blue">
    <div class="brand"><span class="mark"></span><span>Coastal Imaging Partners of Brazos, LLC</span></div>
  </section>

  <section class="piece folder-front">
    <div class="brand"><span class="mark"></span><span>Coastal Imaging Partners of Brazos, LLC</span></div>
    <div class="flap"></div>
  </section>

  <section class="piece folder-open">
    <div class="panel left"><div class="pocket"></div></div>
    <div class="panel right">
      <div class="pocket"></div>
      <div class="slot-card">
        <div class="brand"><span class="mark"></span><span>Coastal Imaging Partners of Brazos, LLC</span></div>
      </div>
    </div>
  </section>

</main>
</body>
</html>
```